Pharmacist turned chef in Key West Fl needs a logo design

I am looking for a professional looking business card that says who I am and what I do. For example Chef Dale Morrow, natural organic and health supportive cooking. Phone 305-617-4289 email dalemorrow@quillpost.example web www.thehearthremedy.example, Key West fl. The color or colors should have some green and other colors that look good together that stimulate appetite and give a clean healthy image. To help with a thought process, words like food as medicine, medicine is food, good nutrition is health but at the same time I do not want a lot of medical symbols that me it look clinical. Any questions please contact me.

```html
<!DOCTYPE html>
<html lang="en">
<head>
<meta charset="utf-8">
<title>Chef Dale Morrow – Business Card</title>
<link rel="stylesheet" href="https://fonts.googleapis.com/css2?family=Open+Sans:wght@400;700&family=Oxygen:wght@400&display=swap">
<style>
  :root {
    --paper: #ffffff;
    --frame: #2b2b2b;
    --orange: #ef7d00;
    --green: #b0cb05;
    --green-soft: rgba(140, 175, 10, 0.45);
    --ink: #1e1e1e;
    --icon-bg: #ffffff;
  }
  * { margin: 0; padding: 0; box-sizing: border-box; }
  html, body {
    width: 1200px;
    height: 780px;
    overflow: hidden;
    background: var(--paper);
  }
  .canvas {
    position: relative;
    width: 1200px;
    height: 780px;
    border: 2px solid var(--frame);
    background: var(--paper);
  }
  .card {
    position: absolute;
    left: 55px;
    top: 53px;
    width: 1089px;
    height: 673px;
    border: 1.5px solid var(--frame);
    overflow: hidden;
    background: var(--green);
  }
  .card__header {
    position: absolute;
    left: 0; top: 0;
    width: 100%;
    height: 347px;
    background: var(--orange);
  }
  .brand-mark {
    position: absolute;
    left: 108px;
    top: 140px;
    width: 156px;
    height: 156px;
    border-radius: 50%;
    background: #7cbf2a;
  }
  .tagline {
    position: absolute;
    left: 280px;
    top: 168px;
    font-family: "Oxygen", sans-serif;
    font-weight: 400;
    font-size: 52px;
    line-height: 60px;
    letter-spacing: 0.5px;
    color: var(--ink);
    text-transform: uppercase;
  }
  .card__body {
    position: absolute;
    left: 0; top: 347px;
    width: 100%;
    height: 326px;
  }
  .backdrop-shape {
    position: absolute;
    left: -30px;
    top: -10px;
    width: 420px;
    height: 420px;
    border-radius: 50%;
    background: var(--green-soft);
    opacity: 0.35;
  }
  .chef-name {
    position: absolute;
    left: 61px;
    top: 118px;
    font-family: "Open Sans", sans-serif;
    font-weight: 700;
    font-size: 37px;
    color: var(--ink);
  }
  .contact-list {
    position: absolute;
    left: 461px;
    top: 55px;
    list-style: none;
  }
  .contact-item {
    display: flex;
    align-items: center;
    height: 67px;
  }
  .contact-icon {
    width: 35px;
    height: 35px;
    border-radius: 7px;
    background: var(--icon-bg);
    display: flex;
    align-items: center;
    justify-content: center;
    margin-right: 16px;
    flex-shrink: 0;
  }
  .contact-icon svg { width: 22px; height: 22px; }
  .contact-text {
    font-family: "Open Sans", sans-serif;
    font-weight: 400;
    font-size: 34px;
    color: var(--ink);
  }
</style>
</head>
<body>
  <div class="canvas">
    <section class="card">
      <header class="card__header">
        <div class="brand-mark" aria-hidden="true"></div>
        <h1 class="tagline">Natural organic and<br>health supportive cooking</h1>
      </header>
      <div class="card__body">
        <div class="backdrop-shape" aria-hidden="true"></div>
        <p class="chef-name">Chef Dale Morrow</p>
        <ul class="contact-list">
          <li class="contact-item">
            <span class="contact-icon">
              <svg viewBox="0 0 24 24" aria-hidden="true"><path d="M6.6 3.5l2.6 3.4-1.6 2c1 2.3 2.8 4.3 5.2 5.6l1.9-1.6 3.5 2.4-1.3 3.2c-6.6-.3-12.6-6.8-12.9-13.4z" fill="#1e1e1e"/></svg>
            </span>
            <span class="contact-text">305-617-4289</span>
          </li>
          <li class="contact-item">
            <span class="contact-icon">
              <svg viewBox="0 0 24 24" aria-hidden="true"><rect x="2.5" y="5.5" width="19" height="13" fill="#1e1e1e"/><path d="M3 6l9 7 9-7" fill="none" stroke="#fff" stroke-width="1.4"/><path d="M3 18l7-6M21 18l-7-6" stroke="#fff" stroke-width="1.2"/></svg>
            </span>
            <span class="contact-text">dalemorrow@quillpost.example</span>
          </li>
          <li class="contact-item">
            <span class="contact-icon">
              <svg viewBox="0 0 24 24" aria-hidden="true" fill="none" stroke="#1e1e1e" stroke-width="1.4"><circle cx="12" cy="12" r="9"/><ellipse cx="12" cy="12" rx="4" ry="9"/><path d="M3 12h18M4.5 7.5h15M4.5 16.5h15M12 3v18"/></svg>
            </span>
            <span class="contact-text">www.thehearthremedy.example</span>
          </li>
        </ul>
      </div>
    </section>
  </div>
</body>
</html>
```